Web Design Project

New website for Aged Care business.

Easy buttons to

1.book appointment

2.request a callback

3.view services

think elderly people using it, or family members

we like the colours of 'tidewell' website

and the middle image and call to action buttons of the rons edging website.

we'd like a rotating image similar to the rons edging but bigger size.

http://www.tidewell.org.au/

http://www.ronsedging.net/

Reason: need to have a meeting with our staff to decide - i'm overseas..

Target Market(s)

elderly people and families of elderly people with enough money to pay for the services offered.

Industry/Entity Type

Business

Requirements
Must have
• contemporary and clean design

```html
<!DOCTYPE html>
<html lang="en">
<head>
<meta charset="utf-8">
<title>Harlow Care</title>
<link rel="stylesheet" href="https://fonts.googleapis.com/css2?family=Source+Sans+3:wght@400;600&display=swap">
<style>
:root{
  --sky:#139bd3;
  --sky-deep:#0e86bd;
  --nav-dark:#0f5f86;
  --nav-mid:#1a7aa6;
  --frame:#0d6f9c;
  --accent:#1aa0d4;
  --accent-dark:#0b7fb0;
  --text:#4a4a4a;
  --white:#ffffff;
  --line:#dcdcdc;
}
*{margin:0;padding:0;box-sizing:border-box}
html,body{width:1152px;height:1200px;overflow:hidden}
body{position:relative;background:var(--white);font-family:"Source Sans 3",Arial,sans-serif;color:var(--text)}
.band-top{position:absolute;left:0;top:0;width:1152px;height:326px;background:linear-gradient(#1aa3dc,var(--sky))}
.band-foot{position:absolute;left:0;top:1054px;width:1152px;height:146px;background:linear-gradient(var(--sky),var(--sky-deep))}
.brand{position:absolute;left:146px;top:28px;font-size:33px;color:var(--white);font-weight:400;letter-spacing:.2px}
.follow{position:absolute;left:866px;top:35px;display:flex;align-items:center;gap:8px;color:var(--white);font-size:13px}
.follow span.lbl{margin-right:8px}
.follow i{display:block;width:16px;height:16px;border-radius:3px;background:rgba(255,255,255,.75)}
.nav{position:absolute;left:132px;top:96px;width:893px;height:39px;border-radius:6px;background:linear-gradient(var(--nav-mid),var(--nav-dark));box-shadow:0 2px 3px rgba(0,0,0,.25);display:flex;align-items:center}
.nav a{color:var(--white);text-decoration:none;font-size:13px;height:39px;line-height:39px;padding:0 18px;border-right:1px solid rgba(0,0,0,.25)}
.nav a:first-child{padding-left:17px}
.search{position:absolute;left:599px;top:9px;width:263px;height:21px;border-radius:6px;background:var(--white);font-size:12px;color:#2a7fa8;line-height:21px;padding-left:13px}
.search svg{position:absolute;right:9px;top:3px}
.slider{position:absolute;left:132px;top:150px;width:893px;height:409px;border-radius:6px;background:var(--frame);box-shadow:0 2px 4px rgba(0,0,0,.3)}
.slide{position:absolute;left:6px;top:6px;width:879px;height:395px;border-radius:6px;background:linear-gradient(100deg,#8b9a6a 0%,#d9d0c0 35%,#e8ded0 55%,#8c9272 75%,#5b4a3c 100%)}
.dots{position:absolute;left:380px;top:393px;display:flex;gap:4px}
.dots i{width:15px;height:15px;border-radius:50%;background:var(--white);border:1px solid #bbb}
.dots i.on{background:#e2572a;border:3px solid var(--white);box-shadow:0 0 0 1px #bbb}
.quick{position:absolute;left:30px;top:28px;display:flex;flex-direction:column;gap:10px}
.quick a{display:block;width:210px;height:42px;line-height:42px;padding-left:16px;border-radius:5px;background:var(--accent);border-bottom:3px solid var(--accent-dark);color:var(--white);font-size:16px;font-weight:600;text-decoration:none;box-shadow:0 2px 4px rgba(0,0,0,.25)}
.card{position:absolute;top:571px;height:273px;background:var(--white);border:1px solid #e2e2e2;box-shadow:0 1px 4px rgba(0,0,0,.2)}
.card h2{height:50px;line-height:50px;padding-left:19px;font-size:18px;font-weight:400;color:var(--accent);background:linear-gradient(#f4f4f4,#fff);border-bottom:1px dashed var(--line)}
.card .pic{position:absolute;left:18px;top:68px;width:247px;height:94px}
.card p{position:absolute;left:17px;top:172px;width:252px;font-size:11.8px;line-height:17px;text-align:justify;letter-spacing:-.1px}
.card .more{position:absolute;left:174px;top:256px;width:91px;height:28px;background:var(--accent);color:var(--white);font-size:12.5px;line-height:28px;text-align:center;text-decoration:none}
.news ul{list-style:none;position:absolute;left:10px;top:62px;width:258px}
.news li{position:relative;padding-left:22px;font-size:12px;line-height:17px;margin-bottom:18px;text-align:justify}
.news li svg{position:absolute;left:0;top:5px}
.welcome{position:absolute;left:132px;top:875px;width:895px;height:207px;background:var(--white);border:1px solid #e2e2e2}
.welcome h2{position:absolute;left:19px;top:12px;font-size:18px;font-weight:400;color:var(--accent)}
.welcome hr{position:absolute;left:19px;top:43px;width:855px;border:0;border-top:1px dashed var(--line)}
.welcome p{position:absolute;left:20px;top:56px;width:578px;font-size:12px;line-height:21.4px;text-align:justify}
.welcome .pic{position:absolute;left:617px;top:67px;width:262px;height:121px;background:#b3b3b3;padding:5px}
.welcome .pic div{width:100%;height:100%;background:linear-gradient(90deg,#7a4a3a,#c79a7a 45%,#e3c9a2 60%,#6f6a70)}
.foot-nav{position:absolute;left:0;top:1118px;width:1118px;text-align:center;font-size:12.5px;color:var(--white)}
.foot-nav a{color:var(--white);text-decoration:none;margin:0 8px}
.copy{position:absolute;left:0;top:1146px;width:1118px;text-align:center;font-size:12px;color:var(--white)}
</style>
</head>
<body>
<div class="band-top"></div>
<div class="band-foot"></div>

<header>
  <div class="brand">Harlow Care</div>
  <div class="follow"><span class="lbl">Follow Us</span><i></i><i></i><i></i><i></i></div>
  <nav class="nav">
    <a href="#">Care and Support</a>
    <a href="#">Retirement Living</a>
    <a href="#">Our Locations</a>
    <a href="#">Our Community</a>
    <a href="#">About Us</a>
    <div class="search">Search
      <svg width="15" height="15" viewBox="0 0 15 15"><circle cx="6" cy="6" r="4.2" fill="none" stroke="#1b7fae" stroke-width="2"/><line x1="9" y1="9" x2="13.5" y2="13.5" stroke="#1b7fae" stroke-width="2.6" stroke-linecap="round"/></svg>
    </div>
  </nav>
</header>

<section class="slider">
  <div class="slide" role="img" aria-label="Elderly couple seated on a sofa talking with a care advisor"></div>
  <div class="quick">
    <a href="#">Book an Appointment</a>
    <a href="#">Request a Callback</a>
    <a href="#">View Our Services</a>
  </div>
  <div class="dots"><i class="on"></i><i></i><i></i><i></i><i></i></div>
</section>

<article class="card" style="left:132px;width:287px">
  <h2>Care and Support</h2>
  <div class="pic" role="img" aria-label="Care staff member at an office desk" style="background:linear-gradient(90deg,#c9a67c,#e8d6c0 50%,#f1ece6)"></div>
  <p>Our professional residential and community care staff can provide you or your loved one with the quality of life and independence you desire when you are unable to manage on your own.</p>
  <a class="more" href="#">Read More &gt;&gt;</a>
</article>

<article class="card" style="left:434px;width:286px">
  <h2>Retirement Living</h2>
  <div class="pic" role="img" aria-label="Retired couple sitting on a park bench among trees" style="background:linear-gradient(90deg,#3f7a2c,#8fbf6a 50%,#4c8a34)"></div>
  <p>Offering you freedom to manage your daily leisure and social activities with the added benefits of shared recreational facilities and worry-free home maintenance.</p>
  <a class="more" href="#">Read More &gt;&gt;</a>
</article>

<article class="card news" style="left:737px;width:288px">
  <h2>News</h2>
  <ul>
    <li><svg width="12" height="11" viewBox="0 0 12 11"><rect x=".5" y=".5" width="11" height="10" fill="#f3f3f3" stroke="#aaa"/><path d="M3 3.5h6M3 5.5h6M3 7.5h6" stroke="#999"/></svg>23 April 2012, Pathway Online<br>YOUNG clients and some staff of Tidewell Ridgeway Valley Community Care have been ...</li>
    <li><svg width="12" height="11" viewBox="0 0 12 11"><rect x=".5" y=".5" width="11" height="10" fill="#f3f3f3" stroke="#aaa"/><path d="M3 3.5h6M3 5.5h6M3 7.5h6" stroke="#999"/></svg>21 April 2012, Bayside Coast Chronicle<br>MAJOR aged care reforms announced by Prime Minister Helen Marsh yesterday have been ...</li>
    <li><svg width="12" height="11" viewBox="0 0 12 11"><rect x=".5" y=".5" width="11" height="10" fill="#f3f3f3" stroke="#aaa"/><path d="M3 3.5h6M3 5.5h6M3 7.5h6" stroke="#999"/></svg>Group helps members cope<br>17 April 2012, Bayside Coast Chronicle<br>ONE in every 350 people in Australia ..</li>
  </ul>
</article>

<section class="welcome">
  <h2>Welcome to our site</h2>
  <hr>
  <p>There was no doubting the degree of demand within the community for what the Tidewell Nursing Service was able to offer. The organisation rapidly expanded and diversified its capabilities to meet those needs. As community needs grew so did the Service, and it rapidly expanded across the State. In 1977, with the union of the Presbyterian and Methodist Churches, the Tidewell Nursing Service came under the banner of the United Fellowship Church in Australia, Queensland Synod. The name 'Tidewell' was chosen to retain some of that identity but also reflect the diversity of compassionate caring services offered by the organisation.</p>
  <div class="pic"><div role="img" aria-label="Smiling mature couple outdoors at sunset"></div></div>
</section>

<footer>
  <div class="foot-nav"><a href="#">Care and Support</a>|<a href="#">Retirement Living</a>|<a href="#">Our Locations</a>|<a href="#">Our Community</a>|<a href="#">About Us</a></div>
  <div class="copy">Copyrights @ 2012 All Rights Reserved</div>
</footer>
</body>
</html>
```